American New Media Company Card Redesign

Our company business cards have grown stale and are in dire need of an update/refresh. The company, Webline Holdings, is an American new media company that owns and operates hundreds of websites that focus on four core verticals: Automotive, Health, Legal, and Home/Travel. We would like our new cards to convey our brand diversity in some way, while also maintaining a professional corporate feel (let's be real a lot of people in sales/legal will pass these around the most).

Learn more about us at www.weblineholdings-example.com

Target Market(s)

Corporate / Tech - We are located in Quartz Cove.

Card will be used by various teams including Legal, Marketing, HR, Sales, & Devs in all four of our verticals.

Industry/Entity Type

Internet

Contact Information for Business Card

DIRECTION:
Here are things we would like to see:

1) "Traditional Facelift" - Similar layout to current design (with select major brands on back - let me know if you want to discuss which brands), basically a facelift of current design

2) "Modern Minimalist" - Fresh design that does not include any of our brands on card (only WH logo) in a modern minimalist, clean format.

3) "Freeform" - A more wildcard design. Could include select brands or not, could be vertically oriented, etc. More creative and edgy.

TOP BRANDS:
- MotorPick, Vehicle Loan Rapid, The Wheel Junction
- NetClin, Clinora, ePhysix
- Brenlow’s Travel, Jetchatter, Make It Solo
- Zell, Tarv, Counselhub.example, Pembrook Larkwell

FOR REFERENCE:

Font styles to use
Sans Serif

Colors
0355a3

Requirements
Must have
• FUNCTIONALITY:
• The cards need a Name, Title, E-mail Address, and 1 to 3 lines for phone numbers (some in the office do have extensions).
• OUR LOGO:
• - Webline Holdings - Corporate Logo
Nice to have
• Our Address:
• 412 S Harbor Ridge Boulevard, 6TH FLOOR
• (But not totally necessary).

```html
<!DOCTYPE html>
<html lang="en">
<head>
<meta charset="utf-8">
<title>Webline Holdings Business Card</title>
<link rel="stylesheet" href="https://fonts.googleapis.com/css2?family=PT+Sans:wght@400;700&display=swap">
<style>
  :root {
    --brand-blue: #0355a3;
    --brand-blue-soft: #cfe0f1;
    --brand-blue-faint: #eef4fa;
    --paper: #ffffff;
    --edge: #9eaeae;
    --mark-grey: #8a8f90;
  }
  * { box-sizing: border-box; margin: 0; padding: 0; }
  html, body { width: 1200px; height: 800px; overflow: hidden; background: var(--paper); }
  body { position: relative; font-family: "PT Sans", sans-serif; }

  .card {
    position: absolute;
    top: 27px;
    width: 537px;
    height: 751px;
    border: 1.5px solid var(--edge);
    overflow: hidden;
  }
  .card--front { left: 25px; background: var(--brand-blue); color: var(--paper); }
  .card--back { left: 637px; background: var(--paper); }

  .world-map {
    position: absolute;
    left: 0; top: 0;
    width: 100%; height: 300px;
    background: linear-gradient(180deg, var(--brand-blue-soft) 0%, #6f9dcb 55%, var(--brand-blue) 100%);
  }

  .identity { position: absolute; left: 47px; top: 393px; }
  .identity__name { font-size: 36px; font-weight: 700; letter-spacing: 3px; line-height: 40px; }
  .identity__title { font-size: 22.5px; font-weight: 400; letter-spacing: 0.5px; line-height: 28px; }

  .contact { position: absolute; left: 47px; top: 494px; list-style: none; }
  .contact li, .address li { font-size: 16.5px; letter-spacing: 0.5px; line-height: 30px; }
  .address { position: absolute; left: 47px; top: 616px; list-style: none; }

  .brand-mark {
    position: absolute;
    display: flex;
    align-items: center;
    gap: 8px;
    width: 150px;
    font-size: 17px;
    font-weight: 700;
    line-height: 19px;
  }
  .brand-mark__dot { width: 30px; height: 30px; border-radius: 50%; flex: none; }
  .card--front .brand-mark { left: 355px; top: 651px; color: var(--paper); }
  .card--front .brand-mark__dot { background: var(--paper); }
  .card--back .brand-mark { left: 351px; top: 651px; color: var(--mark-grey); }
  .card--back .brand-mark__dot { background: var(--mark-grey); }

  .network-art {
    position: absolute;
    left: 45px; top: 38px;
    width: 455px; height: 225px;
    background: linear-gradient(180deg, var(--brand-blue-soft) 0%, var(--brand-blue-faint) 100%);
  }
</style>
</head>
<body>

<section class="card card--front">
  <div class="world-map" role="img" aria-label="World map in white across the top of the card"></div>

  <header class="identity">
    <h1 class="identity__name">JOHN SMITH</h1>
    <p class="identity__title">SOMETHING MANAGER</p>
  </header>

  <ul class="contact">
    <li>JOHN@WEBLINE.EXAMPLE</li>
    <li>TEL 555 555 5555</li>
    <li>FAX 555 555 5555</li>
    <li>CELL 555 555 5555</li>
  </ul>

  <ul class="address">
    <li>412 S HARBOR RIDGE BLVD</li>
    <li>6TH FLOOR, QUARTZ COVE</li>
    <li>CALIFORNIA 90412</li>
  </ul>

  <div class="brand-mark">
    <span class="brand-mark__dot"></span>
    <span>Webline Holdings</span>
  </div>
</section>

<section class="card card--back">
  <div class="network-art" role="img" aria-label="Illustration of dotted points linked by arcs, suggesting a global network"></div>

  <div class="brand-mark">
    <span class="brand-mark__dot"></span>
    <span>Webline Holdings</span>
  </div>
</section>

</body>
</html>
```